property maintenance company covering all trades Plumbing,heating ,electrical building carpentry

business cards

Target Market(s)

DOMESTIC HOUSEHOLDS

Industry/Entity Type

Property Maintenance

Contact Information for Business Card

dorian Pellow
07815 390461
Bramwick Property Maintenace

Font styles to use
Sans Serif

Colors
eda3c7
d2a4cc
b7a5cd

```html
<!DOCTYPE html>
<html lang="en">
<head>
<meta charset="utf-8">
<title>Bramwick Property Maintenace – Business Card</title>
<link rel="stylesheet" href="https://fonts.googleapis.com/css2?family=Lato:wght@300;400;700&display=swap">
<style>
  :root {
    --page-bg: #e9e4e6;
    --card-bg: #f6f1f4;
    --rose: #eda3c7;
    --rose-deep: #d67aa3;
    --orchid: #d2a4cc;
    --lavender: #b7a5cd;
    --ink: #7d7192;
    --ink-soft: #8f84a3;
    --accent: #c95d8d;
    --circle: #fbf8fa;
    --white: #ffffff;
  }
  * { margin: 0; padding: 0; box-sizing: border-box; }
  html, body {
    width: 1200px;
    height: 970px;
    overflow: hidden;
    background: var(--page-bg);
    font-family: "Lato", sans-serif;
  }
  .card {
    position: absolute;
    left: 80px;
    top: 189px;
    width: 1040px;
    height: 592px;
    background: var(--card-bg);
    overflow: hidden;
    box-shadow: 0 10px 30px rgba(90, 70, 90, 0.18);
  }
  .card__side-band {
    position: absolute;
    left: 0; top: 0;
    width: 215px; height: 100%;
    background: linear-gradient(180deg, var(--rose-deep), var(--rose));
  }
  .card__emblem-disc {
    position: absolute;
    left: 5px; top: 30px;
    width: 530px; height: 530px;
    border-radius: 50%;
    background: var(--circle);
    display: flex;
    align-items: center;
    justify-content: center;
  }
  .brand-name {
    width: 300px;
    text-align: center;
    font-size: 34px;
    font-weight: 400;
    line-height: 1.3;
    letter-spacing: 1px;
    color: var(--accent);
  }
  .name-band {
    position: absolute;
    left: 567px; top: 83px;
    width: 473px; height: 94px;
    border-radius: 47px 0 0 47px;
    background: linear-gradient(90deg, var(--rose-deep), var(--rose));
    text-align: right;
    padding: 12px 77px 0 0;
  }
  .name-band__name {
    font-size: 31px;
    font-weight: 700;
    color: var(--white);
    line-height: 1.05;
  }
  .name-band__title {
    font-size: 25px;
    font-weight: 300;
    color: var(--white);
    line-height: 1.15;
  }
  .contact {
    position: absolute;
    left: 582px;
    width: 381px;
    text-align: right;
    font-size: 26px;
    line-height: 35px;
    color: var(--ink);
  }
  .contact--address { top: 271px; }
  .contact--reach { top: 367px; }
  .contact--web { top: 463px; font-size: 25px; }
  .contact__tag { color: var(--accent); }
  .divider {
    position: absolute;
    left: 582px;
    width: 381px;
    height: 2px;
    background: var(--orchid);
  }
  .divider--first { top: 349px; }
  .divider--second { top: 451px; }
</style>
</head>
<body>
  <section class="card">
    <div class="card__side-band"></div>
    <div class="card__emblem-disc">
      <p class="brand-name">Bramwick Property Maintenace</p>
    </div>

    <header class="name-band">
      <p class="name-band__name">Dorian Pellow</p>
      <p class="name-band__title">Chief Executive Officer</p>
    </header>

    <p class="contact contact--address">0000 Youe Address,2nd Ste.<br>Larchford, Texas 1234</p>
    <div class="divider divider--first"></div>
    <p class="contact contact--reach">07815 390461 <span class="contact__tag">:P</span><br>your@companymail.com <span class="contact__tag">:E</span></p>
    <div class="divider divider--second"></div>
    <p class="contact contact--web">www.<span class="contact__tag">companyweb</span>.com</p>
  </section>
</body>
</html>
```